Building and Maintenance Company requires a flyer design, Specialising in domestic and commercial bu

We need a flyer design for a company based in Melbourne Victoria, we want to send the flyer out to businesses to obtain more work.

KEV Building and Construction provides the solution for all your building and maintenance needs

We have a professional and highly regarded team of reliable and skilled tradesmen who specialise in building services, domestic and commercial maintenance and gardening in Victoria and Tasmania.

Include our contact details;
0412 738 206
info@kevbuilding.example.au
www.kevbuilding.example.au

Target Market(s)

Domestic and Commercial Clients looking for building maintenance, window cleaning or gardening

Industry/Entity Type

It Company

Font styles to use
Sans Serif

Colors
33b8a4
474747
ffffff

Requirements
Must have
• Images and colour
Nice to have
• We would like the flyer to have our contact details on it.
• Colourful
• Clearly explains what we do, which is, 'KEV Building and Construction provides the solution for all your building, maintenance and gardening needs.'

```html
<!DOCTYPE html>
<html lang="en">
<head>
<meta charset="utf-8">
<title>KEV Building and Construction – Flyer</title>
<link rel="stylesheet" href="https://fonts.googleapis.com/css2?family=Rajdhani:wght@600&family=Oswald:wght@500&family=Lato:ital,wght@0,300;0,400;1,400&display=swap">
<style>
  :root {
    --teal: #33b8a4;
    --teal-bright: #2fc6c0;
    --charcoal: #474747;
    --charcoal-deep: #2f2f2f;
    --light: #f2f2f2;
    --mid: #c8c8c8;
    --white: #ffffff;
  }
  * { margin: 0; padding: 0; box-sizing: border-box; }
  html, body { width: 855px; height: 1200px; overflow: hidden; background: var(--white); }
  .flyer { position: relative; width: 855px; height: 1200px; overflow: hidden; font-family: "Lato", sans-serif; }
  .backdrop { position: absolute; inset: 0; }
  .abs { position: absolute; }

  .brand { left: 40px; top: 58px; width: 300px; color: var(--white); font-family: "Rajdhani", sans-serif; font-weight: 600; line-height: 0.95; }
  .brand-short { display: block; font-size: 150px; letter-spacing: 4px; }
  .brand-rest { display: block; font-size: 37px; letter-spacing: 4px; text-transform: uppercase; margin-top: 6px; }

  .service-badge { left: 37px; top: 315px; width: 303px; height: 81px; border: 2px solid var(--teal); border-radius: 14px;
    color: var(--white); font-weight: 300; font-size: 24px; line-height: 29px; text-align: center; display: flex; align-items: center; justify-content: center; }

  .call-line { left: 42px; top: 424px; font-size: 31px; font-weight: 400; color: var(--white); letter-spacing: -0.5px; }
  .call-line .number { color: var(--teal-bright); font-weight: 300; }

  .tagline { left: 47px; top: 778px; width: 520px; font-style: italic; font-size: 34px; line-height: 42px; color: var(--charcoal); letter-spacing: -0.3px; }

  .contact-box { left: 567px; top: 855px; width: 288px; height: 116px; background: var(--charcoal-deep); border-top: 3px solid var(--white); border-bottom: 3px solid var(--white); padding: 10px 0 0 23px; color: var(--white); overflow: hidden; }
  .contact-heading { font-family: "Oswald", sans-serif; font-weight: 500; font-size: 33px; line-height: 38px; letter-spacing: 0; white-space: nowrap; }
  .contact-phone { font-weight: 300; font-size: 37px; line-height: 38px; color: var(--teal-bright); white-space: nowrap; letter-spacing: -0.5px; }
  .contact-email { font-size: 17px; line-height: 22px; white-space: nowrap; }

  .about { left: 580px; top: 1012px; width: 245px; font-size: 12px; line-height: 14.6px; color: var(--white); text-align: right; letter-spacing: -0.2px; }

  .footer-link { left: 0; top: 1142px; width: 855px; text-align: center; font-size: 21px; letter-spacing: 4.6px; color: var(--white); font-weight: 400; white-space: nowrap; }
</style>
</head>
<body>
<main class="flyer">
  <svg class="backdrop" width="855" height="1200" viewBox="0 0 855 1200">
    <defs>
      <linearGradient id="lightFloor" x1="0" y1="0" x2="1" y2="1">
        <stop offset="0" stop-color="#fafafa"/>
        <stop offset="1" stop-color="#bdbdbd"/>
      </linearGradient>
      <linearGradient id="darkTop" x1="0" y1="0" x2="1" y2="1">
        <stop offset="0" stop-color="#3a3a3a"/>
        <stop offset="0.6" stop-color="#575757"/>
        <stop offset="1" stop-color="#3c3c3c"/>
      </linearGradient>
      <linearGradient id="tealPanel" x1="0" y1="0" x2="0" y2="1">
        <stop offset="0" stop-color="#2ab7b1"/>
        <stop offset="1" stop-color="#34cfc6"/>
      </linearGradient>
      <linearGradient id="footerBar" x1="0" y1="0" x2="1" y2="0">
        <stop offset="0" stop-color="#3b3b3b"/>
        <stop offset="0.5" stop-color="#575757"/>
        <stop offset="1" stop-color="#3b3b3b"/>
      </linearGradient>
    </defs>

    <rect class="surface-light" width="855" height="1200" fill="url(#lightFloor)"/>
    <polygon class="panel-teal" points="565,500 855,440 855,1120 565,1120" fill="url(#tealPanel)"/>
    <polygon class="band-teal" points="0,602 855,445 855,475 0,632" fill="var(--teal)"/>
    <polygon class="surface-dark" points="0,0 855,0 855,455 0,612" fill="url(#darkTop)"/>

    <polygon class="hero-frame" points="383,0 855,0 855,463 596,494 383,390" fill="var(--teal)"/>
    <polygon class="hero-photo" role="img" aria-label="Photo of a construction worker in hard hat and hi-vis vest cutting with an angle grinder on a rooftop under a cloudy sky"
      points="392,0 855,0 855,455 598,485 392,385" fill="#7d9fbf"/>

    <g class="circle-photo">
      <circle cx="158" cy="611" r="100" fill="var(--white)"/>
      <circle cx="158" cy="611" r="88" fill="var(--teal)"/>
      <circle cx="158" cy="611" r="83" fill="#dedcd6" role="img" aria-label="Photo of building plans on a desk with calculator, ruler and pencils"/>
    </g>
    <g class="circle-photo">
      <circle cx="436" cy="581" r="100" fill="var(--white)"/>
      <circle cx="436" cy="581" r="88" fill="var(--teal)"/>
      <circle cx="436" cy="581" r="83" fill="#d9d6cf" role="img" aria-label="Illustration of a house model with an open roof frame on a blueprint"/>
    </g>
    <g class="circle-photo">
      <circle cx="718" cy="522" r="105" fill="var(--white)"/>
      <circle cx="718" cy="522" r="93" fill="var(--teal)"/>
      <circle cx="718" cy="522" r="88" fill="#e1dccb" role="img" aria-label="Photo of a yellow hard hat resting on rolled plans with a ruler"/>
    </g>

    <rect class="photo-frame" x="592" y="685" width="224" height="137" fill="var(--white)"/>
    <rect class="photo" x="597" y="690" width="214" height="127" fill="#9fc3df" role="img" aria-label="Photo of a woman cleaning a window with a yellow cloth"/>

    <rect class="strip-frame" x="43" y="953" width="483" height="109" fill="var(--teal)"/>
    <rect class="strip-inner" x="48" y="958" width="473" height="99" fill="var(--white)"/>
    <rect class="strip-photo" x="52" y="962" width="465" height="91" fill="#8aa979" role="img" aria-label="Photo strip of tradesmen hedge trimming, painting, using a tool belt and pruning plants"/>

    <rect class="footer-rule" x="0" y="1116" width="855" height="5" fill="var(--teal)"/>
    <rect class="footer-bar" x="0" y="1121" width="855" height="79" fill="url(#footerBar)"/>
  </svg>

  <h1 class="brand abs">
    <span class="brand-short">KEV</span>
    <span class="brand-rest">Building and Construction</span>
  </h1>

  <div class="service-badge abs">Domestic and Commercial<br>Maintenance</div>

  <p class="call-line abs">CALL <span class="number">0412 738 206</span></p>

  <p class="tagline abs">Specialising in domestic and commercial building maintenance, gardening and window cleaning.</p>

  <section class="contact-box abs">
    <h2 class="contact-heading">CONTACT US TODAY</h2>
    <p class="contact-phone">0412 738 206</p>
    <p class="contact-email">info@kevbuilding.example.au</p>
  </section>

  <p class="about abs">We have a professional and highly regarded team of reliable and skilled tradesmen who specialise in building services, domestic and commercial maintenance and gardening in Victoria and Tasmania.</p>

  <p class="footer-link abs">Please visit us to know more at - www.kevbuilding.example.au</p>
</main>
</body>
</html>
```